NEW YORK Plumbing/utility company 10 year anniversary business card

Looking For simple back and front business card would like to include a few things in description
We offer 24/7 emergency service
residential
commercial
industrial
municipal
services offered
Plumbing
hydro excavation
hydro jetting
Well pumps
Sewer pumps
water mains
sewer mains

```html
<!DOCTYPE html>
<html lang="en">
<head>
<meta charset="utf-8">
<title>Ridgeline Water &amp; Sewer – Business Card</title>
<link rel="stylesheet" href="https://fonts.googleapis.com/css2?family=Raleway:wght@500;600;700&family=Roboto+Condensed:wght@500;700&family=Courgette&display=swap">
<style>
  :root {
    --page-bg: #2a2a2a;
    --navy: #0e5d9e;
    --blue-dark: #0a5a9c;
    --blue-mid: #1f78bb;
    --sky: #0cacee;
    --ink: #2b2b33;
    --white: #ffffff;
  }
  * { box-sizing: border-box; margin: 0; padding: 0; }
  html, body {
    width: 1200px; height: 900px; overflow: hidden;
    background: var(--page-bg);
    font-family: "Raleway", sans-serif;
  }
  .canvas { position: relative; width: 1200px; height: 900px; }

  .card {
    position: absolute; left: 250px; width: 700px; height: 400px;
    overflow: hidden;
  }
  .card--back {
    top: 30px;
    background: linear-gradient(120deg, var(--blue-dark) 0%, var(--blue-mid) 100%);
    color: var(--white);
  }
  .card--front { top: 470px; background: var(--white); }

  .brand-name {
    position: absolute;
    font-family: "Raleway", sans-serif;
    font-weight: 700;
    font-size: 34px;
    line-height: 1.2;
    letter-spacing: 3px;
    text-transform: uppercase;
    text-align: center;
  }
  .card--back .brand-name { left: 50px; top: 140px; width: 330px; color: var(--white); }
  .card--front .brand-name { left: 170px; top: 95px; width: 360px; color: var(--navy); }

  .services { position: absolute; left: 425px; top: 110px; }
  .services__title {
    font-size: 21px; font-weight: 600; letter-spacing: 1px;
    text-transform: uppercase; margin-bottom: 6px;
  }
  .services__list { list-style: none; }
  .services__item {
    display: flex; align-items: center; gap: 10px;
    font-size: 17px; font-weight: 600; letter-spacing: 1px;
    text-transform: uppercase; line-height: 27px;
  }
  .drop { width: 10px; height: 13px; flex: none; }

  .badge { position: absolute; left: 535px; top: 0; width: 120px; height: 100px; }
  .badge__number {
    position: absolute; left: 555px; top: 6px; width: 80px; text-align: center;
    font-family: "Roboto Condensed", sans-serif; font-weight: 700;
    font-size: 44px; color: var(--white); line-height: 1;
  }
  .badge__number sup { font-size: 12px; vertical-align: 26px; }
  .anniversary {
    position: absolute; left: 500px; top: 100px; width: 180px; text-align: center;
    font-family: "Courgette", cursive; font-size: 30px; color: var(--navy);
  }

  .band { position: absolute; left: 0; top: 232px; width: 700px; height: 50px; }
  .emergency {
    position: absolute; left: 160px; top: 240px; width: 440px; height: 36px;
    display: flex; align-items: center; justify-content: center;
    font-family: "Roboto Condensed", sans-serif; font-weight: 500;
    font-size: 24px; color: var(--white); text-transform: uppercase;
  }

  .sectors {
    position: absolute; left: 0; top: 312px; width: 700px;
    display: flex; justify-content: center; gap: 16px;
    font-size: 19px; font-weight: 500; color: var(--ink); text-transform: uppercase;
  }
  .sectors__item { display: flex; align-items: center; gap: 6px; }
</style>
</head>
<body>
<main class="canvas">

  <section class="card card--back" aria-label="Card back">
    <p class="brand-name">Ridgeline<br>Water &amp; Sewer</p>
    <div class="services">
      <h2 class="services__title">Services Offered</h2>
      <ul class="services__list">
        <li class="services__item"><svg class="drop" viewBox="0 0 10 13"><path d="M5 0 C7 4 10 6 10 8.5 A5 4.5 0 0 1 0 8.5 C0 6 3 4 5 0Z" fill="#fff"/></svg>Plumbing</li>
        <li class="services__item"><svg class="drop" viewBox="0 0 10 13"><path d="M5 0 C7 4 10 6 10 8.5 A5 4.5 0 0 1 0 8.5 C0 6 3 4 5 0Z" fill="#fff"/></svg>Hydro Excavation</li>
        <li class="services__item"><svg class="drop" viewBox="0 0 10 13"><path d="M5 0 C7 4 10 6 10 8.5 A5 4.5 0 0 1 0 8.5 C0 6 3 4 5 0Z" fill="#fff"/></svg>Hydro Jetting</li>
        <li class="services__item"><svg class="drop" viewBox="0 0 10 13"><path d="M5 0 C7 4 10 6 10 8.5 A5 4.5 0 0 1 0 8.5 C0 6 3 4 5 0Z" fill="#fff"/></svg>Well Pumps</li>
        <li class="services__item"><svg class="drop" viewBox="0 0 10 13"><path d="M5 0 C7 4 10 6 10 8.5 A5 4.5 0 0 1 0 8.5 C0 6 3 4 5 0Z" fill="#fff"/></svg>Sewer Pumps</li>
        <li class="services__item"><svg class="drop" viewBox="0 0 10 13"><path d="M5 0 C7 4 10 6 10 8.5 A5 4.5 0 0 1 0 8.5 C0 6 3 4 5 0Z" fill="#fff"/></svg>Water Mains</li>
        <li class="services__item"><svg class="drop" viewBox="0 0 10 13"><path d="M5 0 C7 4 10 6 10 8.5 A5 4.5 0 0 1 0 8.5 C0 6 3 4 5 0Z" fill="#fff"/></svg>Sewer Mains</li>
      </ul>
    </div>
  </section>

  <section class="card card--front" aria-label="Card front">
    <p class="brand-name">Ridgeline<br>Water &amp; Sewer</p>

    <svg class="badge" viewBox="0 0 120 100" aria-hidden="true">
      <path d="M18 0 H102 V92 L60 74 L18 92 Z" fill="#0e5d9e"/>
      <path d="M30 64 L60 76 L90 64" fill="none" stroke="#0cacee" stroke-width="4"/>
    </svg>
    <p class="badge__number">10<sup>TH</sup></p>
    <p class="anniversary">Anniversary</p>

    <svg class="band" viewBox="0 0 700 50" aria-hidden="true">
      <polygon points="0,4 140,4 152,38 0,38" fill="#0cacee"/>
      <polygon points="560,14 700,14 700,46 548,46" fill="#0cacee"/>
      <polygon points="150,0 600,0 585,50 165,50" fill="#0e5d9e"/>
    </svg>
    <p class="emergency">We offer 24/7 emergency service</p>

    <ul class="sectors">
      <li class="sectors__item"><svg class="drop" viewBox="0 0 10 13"><path d="M5 0 C7 4 10 6 10 8.5 A5 4.5 0 0 1 0 8.5 C0 6 3 4 5 0Z" fill="#0e5d9e"/></svg>Residential</li>
      <li class="sectors__item"><svg class="drop" viewBox="0 0 10 13"><path d="M5 0 C7 4 10 6 10 8.5 A5 4.5 0 0 1 0 8.5 C0 6 3 4 5 0Z" fill="#0e5d9e"/></svg>Commercial</li>
      <li class="sectors__item"><svg class="drop" viewBox="0 0 10 13"><path d="M5 0 C7 4 10 6 10 8.5 A5 4.5 0 0 1 0 8.5 C0 6 3 4 5 0Z" fill="#0e5d9e"/></svg>Industrial</li>
      <li class="sectors__item"><svg class="drop" viewBox="0 0 10 13"><path d="M5 0 C7 4 10 6 10 8.5 A5 4.5 0 0 1 0 8.5 C0 6 3 4 5 0Z" fill="#0e5d9e"/></svg>Municipal</li>
    </ul>
  </section>

</main>
</body>
</html>
```